Vornel Estates - Chat n’ Cheer Thursday Graphic Invite

We need a graphic design for a corporate reception that we are calling Chat n’ Cheer Thursday. The invite should read:

"QBR invites you to join us at Chat n’ Cheer Thursday

Monday, Jan 22nd
6:30 - 8:30 pm EST

Copper Ladle - Lounge Room

48210 E Pelican Grove Rd
Harbor Key, FL 34021

Join us for excellent wine and tasty bites at our semi-annual DAW reception. Swing by whenever you can – timing is casual and we'd love to see you there!"

Please feel free to use fun photos from the Copper Ladle gallery: https://www.copperladlegrill.com/photos

Also, please use the QBR logo attached.

Target Market(s)

Corporate professional

Colors
0054AA
0677BA
7BADD7
CADEEF
E8F1F8

Requirements
Must have
• QBR logo, attached verbiage

```html
<!DOCTYPE html>
<html lang="en">
<head>
<meta charset="utf-8">
<title>QBR – Chat n’ Cheer Thursday Invite</title>
<link rel="stylesheet" href="https://fonts.googleapis.com/css2?family=Great+Vibes&family=Kreon:wght@300;400&display=swap">
<style>
  :root {
    --sky: #5ecbf5;
    --navy: #1a3a8a;
    --frame: #ffffff;
    --brand: #0054aa;
    --text: #ffffff;
    --venue: #ffff00;
    --shadow: rgba(0, 0, 0, 0.75);
  }
  * { margin: 0; padding: 0; box-sizing: border-box; }
  html, body { width: 846px; height: 1200px; overflow: hidden; }
  body { background: #ffffff; }

  .invite {
    position: relative;
    width: 846px;
    height: 1200px;
    overflow: hidden;
    background: linear-gradient(90deg, var(--sky) 0 50.4%, var(--navy) 50.4% 100%);
    font-family: "Kreon", Georgia, serif;
    font-weight: 300;
    color: var(--text);
  }

  .frame {
    position: absolute;
    left: 40px; top: 33px;
    width: 766px; height: 1133px;
    background: var(--frame);
  }

  .venue-photo {
    position: absolute;
    left: 48px; top: 41px;
    width: 750px; height: 1117px;
    background:
      radial-gradient(ellipse 340px 260px at 50% 10%, rgba(255,255,255,0.95), rgba(255,255,255,0.55) 45%, rgba(255,255,255,0) 80%),
      radial-gradient(ellipse 260px 420px at 85% 35%, rgba(150,175,185,0.45), rgba(150,175,185,0) 75%),
      linear-gradient(180deg, #8c7a6c 0%, #5e4a3e 30%, #3a2b24 52%, #2c1d17 66%, #6a3218 82%, #b0521f 100%);
  }

  .content {
    position: absolute;
    inset: 0;
    text-shadow: 2px 3px 4px var(--shadow);
  }

  .line {
    position: absolute;
    left: 0; width: 846px;
    text-align: center;
    white-space: nowrap;
    line-height: 1;
    font-weight: 300;
  }

  .brand {
    position: absolute;
    top: 122px; left: 0; width: 846px;
    display: flex; justify-content: center; align-items: center; gap: 14px;
    text-shadow: none;
  }
  .brand-square {
    width: 40px; height: 40px;
    background: var(--brand);
  }
  .brand-name {
    font-family: "Kreon", Georgia, serif;
    font-weight: 400;
    font-size: 50px;
    line-height: 1;
    color: var(--brand);
  }

  .lead { top: 256px; font-size: 24px; }

  .title {
    font-family: "Great Vibes", cursive;
    font-weight: 400;
    font-size: 122px;
    text-shadow: 3px 5px 6px var(--shadow);
  }
  .title-top { top: 322px; }
  .title-bottom { top: 452px; }

  .date { top: 626px; font-size: 31px; }
  .time { top: 662px; font-size: 31px; }

  .venue { top: 714px; font-size: 31px; }
  .venue-name { color: var(--venue); }
  .street { top: 750px; font-size: 31px; }
  .city { top: 785px; font-size: 31px; }

  .rule {
    position: absolute;
    height: 2px;
    background: var(--text);
    box-shadow: 1px 2px 3px var(--shadow);
  }
  .rule-left { left: 164px; top: 858px; width: 171px; }
  .rule-right { left: 500px; top: 858px; width: 199px; }
  .rule-bottom { left: 164px; top: 971px; width: 535px; }

  .join { top: 837px; font-size: 32px; }
  .offer { font-size: 33px; }
  .offer-one { top: 877px; }
  .offer-two { top: 917px; }

  .note { font-size: 23px; }
  .note-one { top: 993px; }
  .note-two { top: 1024px; }
  .note-three { top: 1055px; }
</style>
</head>
<body>
  <main class="invite">
    <div class="frame"></div>
    <div class="venue-photo" role="img" aria-label="Photo of the Copper Ladle lounge room: a long dining table with grey chairs, candles, a glass wine wall and a warm wooden floor"></div>

    <div class="content">
      <div class="brand">
        <span class="brand-square"></span>
        <span class="brand-name">QBR</span>
      </div>

      <p class="line lead">QBR Invites you to join us at</p>

      <h1 class="line title title-top">Chat N’cheer</h1>
      <p class="line title title-bottom">Thursday</p>

      <p class="line date">Monday, Jan 22nd, 2024</p>
      <p class="line time">6:30-8:30pm Est</p>

      <p class="line venue"><span class="venue-name">@ Copper Ladle</span> - Lounge Room</p>
      <p class="line street">48210 E Pelican Grove Rd</p>
      <p class="line city">Harbor Key, FL 34021</p>

      <span class="rule rule-left"></span>
      <p class="line join">Join us</p>
      <span class="rule rule-right"></span>
      <p class="line offer offer-one">for Excellent Wine and Tasty Bites</p>
      <p class="line offer offer-two">at our Semi-Annual DAW Reception</p>
      <span class="rule rule-bottom"></span>

      <p class="line note note-one">Swing by whenever you can -</p>
      <p class="line note note-two">Timing is Casual</p>
      <p class="line note note-three">and we’d love to see you</p>
    </div>
  </main>
</body>
</html>
```